Shipping Container Sales & Leasing Flyer

We need a flyer that is going to be presented and left behind while prospecting potential customers. The service we are selling is the sale, rental and customization of 20' and 40' shipping containers.

We provide new and used containers to customers for various reasons, mainly storage. We also custom modify containers into storage units, mobile offices, mobile job site storage, command centers, pump houses, garages, living space, the only limit is the customers imagination.

I would like our company logo and phone / email at the bottom but the design should showcase some of the attached images ive provided as examples and have spots where we can list the types of equipment we have for sale and the various types of conversions we can offer.

Please also tie in to the colour scheme of our logo.

Target Market(s)

Moving & Storage, Construction, Contractors, Business to Business, Any business that needs portable storage, Landscapers, Property Maintenance companies.

Industry/Entity Type

Shipping

Font styles to use
Serif
Sans Serif

Requirements
Must have
• Professional feel, clean original design.
Nice to have
• Tie in to our logo colour scheme.
Should not have
• Bulky or crowded look

```html
<!DOCTYPE html>
<html lang="en">
<head>
<meta charset="utf-8">
<title>Torvin Management – Container Flyer</title>
<link href="https://fonts.googleapis.com/css2?family=Archivo+Black&family=Roboto+Condensed:wght@700&family=Oswald:wght@700&family=Lato:ital,wght@0,400;0,700;1,400&display=swap" rel="stylesheet">
<style>
  :root{
    --green:#6a9a3e;
    --green-dark:#3f6b1f;
    --green-light:#8cbf5a;
    --ink:#111111;
    --band:#1b1b1b;
    --paper:#ffffff;
    --panel:#ececec;
    --backdrop:#e9e6e1;
    --text:#1e1e1e;
  }
  *{margin:0;padding:0;box-sizing:border-box}
  html,body{width:907px;height:1200px;overflow:hidden;background:var(--backdrop)}
  .canvas{position:relative;width:907px;height:1200px}
  .flyer{
    position:absolute;left:43px;top:26px;width:730px;height:1023px;
    transform:scale(1.1233);transform-origin:0 0;
    background:var(--paper);overflow:hidden;
    box-shadow:0 4px 14px rgba(0,0,0,.25);
    font-family:"Lato",sans-serif;color:var(--text);
  }
  .brand-panel{position:absolute;left:0;top:0;width:305px;height:360px}
  .brand{position:absolute;left:0;top:70px;width:305px;text-align:center}
  .brand-dot{width:62px;height:62px;border-radius:50%;background:var(--green);margin:0 auto 18px}
  .brand-name{font-family:"Lato",sans-serif;font-weight:700;color:var(--green);font-size:28px;letter-spacing:4px;line-height:1.15}
  .hero-photo{position:absolute;left:305px;top:0;width:425px;height:313px;
    background:linear-gradient(180deg,#c7c9d3 0%,#d9dadd 45%,#b9bbbb 72%,#3f3f42 100%)}
  .headline-band{position:absolute;left:0;top:385px;width:730px;height:128px;
    background:linear-gradient(90deg,#0c0c0c 0%,#2a2a2a 50%,#0c0c0c 100%);text-align:center}
  .headline-top{font-family:"Archivo Black",sans-serif;color:var(--green);font-size:38px;letter-spacing:2px;margin-top:12px;line-height:44px}
  .headline-bottom{font-family:"Roboto Condensed",sans-serif;font-weight:700;color:#fff;font-size:46px;letter-spacing:1px;line-height:56px}
  .offer-tab{position:absolute;left:0;top:528px;width:383px;height:73px;
    background:linear-gradient(90deg,var(--green-dark),var(--green) 70%,var(--green-light));
    clip-path:polygon(0 0,100% 0,82% 100%,0 100%);
    font-family:"Roboto Condensed",sans-serif;font-weight:700;color:#fff;font-size:22px;line-height:25px;padding:10px 0 0 31px}
  .conversions{position:absolute;top:620px;list-style:none;font-style:italic;font-size:16px}
  .conversions li{position:relative;padding-left:22px;height:27.5px;line-height:20px}
  .conversions li svg{position:absolute;left:0;top:3px}
  .conversions.col-a{left:29px}
  .conversions.col-b{left:245px;top:618px}
  .call{position:absolute;left:31px;top:780px}
  .call-label{font-family:"Oswald",sans-serif;font-weight:700;font-size:56px;line-height:60px;color:var(--ink);letter-spacing:1px}
  .call-number{font-family:"Oswald",sans-serif;font-weight:700;font-size:47px;line-height:52px;color:var(--green);letter-spacing:2px;
    text-shadow:1px 1px 0 #bbb,2px 2px 0 #999}
  .container-photo{position:absolute;left:358px;top:713px;width:372px;height:225px;
    background:linear-gradient(160deg,#d8ccab 0%,#c7b892 55%,#a99a74 100%);
    clip-path:polygon(0 22%,55% 0,100% 2%,100% 100%,55% 100%,0 78%)}
  .footer{position:absolute;left:0;top:938px;width:730px;height:85px;
    background:linear-gradient(180deg,#4a4a4a 0%,#1e1e1e 60%,#111 100%)}
  .contact{position:absolute;left:29px;list-style:none;color:#fff;font-size:15px}
  .contact li{height:28px;display:flex;align-items:center;gap:8px}
  .contact{top:14px}
  .deco{position:absolute;left:0;top:0}
</style>
</head>
<body>
<div class="canvas">
  <div class="flyer">
    <svg class="deco" width="730" height="1023" viewBox="0 0 730 1023" aria-hidden="true">
      <defs>
        <linearGradient id="panelGrad" x1="0" y1="0" x2="1" y2="1">
          <stop offset="0" stop-color="#f4f4f4"/><stop offset="1" stop-color="#dcdcdc"/>
        </linearGradient>
        <linearGradient id="chevGrad" x1="0" y1="0" x2="1" y2="0">
          <stop offset="0" stop-color="#8cbf5a"/><stop offset="1" stop-color="#4f8128"/>
        </linearGradient>
      </defs>
      <!-- brand pennant -->
      <polygon points="0,0 305,0 305,360 150,298 0,360" fill="url(#panelGrad)"/>
      <polyline points="0,352 150,292 298,352" fill="none" stroke="var(--green)" stroke-width="9"/>
      <rect x="298" y="0" width="7" height="368" fill="var(--green)"/>
      <!-- line under hero photo -->
      <rect x="305" y="322" width="425" height="8" fill="var(--green)"/>
      <!-- right chevron field -->
      <polygon points="490,513 730,513 730,938 388,938 575,660" fill="url(#chevGrad)"/>
      <polyline points="488,513 573,660 386,935" fill="none" stroke="#ffffff" stroke-width="4"/>
      <!-- lower green rule -->
      <rect x="0" y="925" width="400" height="6" fill="var(--green)"/>
    </svg>

    <div class="brand-panel">
      <div class="brand">
        <div class="brand-dot"></div>
        <div class="brand-name">TORVIN<br>MANAGEMENT</div>
      </div>
    </div>

    <div class="hero-photo" role="img" aria-label="Photo of a white shipping container converted with a sliding glass door"></div>

    <div class="headline-band">
      <div class="headline-top">CUSTOMIZATION OF 20</div>
      <div class="headline-bottom">AND 40' SHIPPING CONTAINERS</div>
    </div>

    <div class="offer-tab">We also custom modify<br>containers into</div>

    <ul class="conversions col-a">
      <li><svg width="14" height="14" viewBox="0 0 14 14"><circle cx="7" cy="7" r="6" fill="none" stroke="var(--green)" stroke-width="1.6"/><path d="M4 7.2l2 2 4-4.4" fill="none" stroke="var(--green)" stroke-width="1.6"/></svg>Storage units</li>
      <li><svg width="14" height="14" viewBox="0 0 14 14"><circle cx="7" cy="7" r="6" fill="none" stroke="var(--green)" stroke-width="1.6"/><path d="M4 7.2l2 2 4-4.4" fill="none" stroke="var(--green)" stroke-width="1.6"/></svg>Mobile offices</li>
      <li><svg width="14" height="14" viewBox="0 0 14 14"><circle cx="7" cy="7" r="6" fill="none" stroke="var(--green)" stroke-width="1.6"/><path d="M4 7.2l2 2 4-4.4" fill="none" stroke="var(--green)" stroke-width="1.6"/></svg>Mobile job site storage</li>
      <li><svg width="14" height="14" viewBox="0 0 14 14"><circle cx="7" cy="7" r="6" fill="none" stroke="var(--green)" stroke-width="1.6"/><path d="M4 7.2l2 2 4-4.4" fill="none" stroke="var(--green)" stroke-width="1.6"/></svg>Command centers</li>
      <li><svg width="14" height="14" viewBox="0 0 14 14"><circle cx="7" cy="7" r="6" fill="none" stroke="var(--green)" stroke-width="1.6"/><path d="M4 7.2l2 2 4-4.4" fill="none" stroke="var(--green)" stroke-width="1.6"/></svg>Pump houses</li>
    </ul>
    <ul class="conversions col-b">
      <li><svg width="14" height="14" viewBox="0 0 14 14"><circle cx="7" cy="7" r="6" fill="none" stroke="var(--green)" stroke-width="1.6"/><path d="M4 7.2l2 2 4-4.4" fill="none" stroke="var(--green)" stroke-width="1.6"/></svg>Garages</li>
      <li><svg width="14" height="14" viewBox="0 0 14 14"><circle cx="7" cy="7" r="6" fill="none" stroke="var(--green)" stroke-width="1.6"/><path d="M4 7.2l2 2 4-4.4" fill="none" stroke="var(--green)" stroke-width="1.6"/></svg>living space</li>
      <li><svg width="14" height="14" viewBox="0 0 14 14"><circle cx="7" cy="7" r="6" fill="none" stroke="var(--green)" stroke-width="1.6"/><path d="M4 7.2l2 2 4-4.4" fill="none" stroke="var(--green)" stroke-width="1.6"/></svg>The only limit is<br>the customers imagination</li>
    </ul>

    <div class="container-photo" role="img" aria-label="Photo of a beige 20 foot shipping container"></div>

    <div class="call">
      <div class="call-label">CALL NOW</div>
      <div class="call-number">0123456789</div>
    </div>

    <div class="footer">
      <ul class="contact">
        <li><svg width="20" height="14" viewBox="0 0 20 14"><rect x="1" y="1" width="18" height="12" fill="none" stroke="var(--green-light)" stroke-width="1.4"/><path d="M1 1l9 7 9-7" fill="none" stroke="var(--green-light)" stroke-width="1.4"/></svg>www.company@mail.com</li>
        <li><svg width="20" height="16" viewBox="0 0 20 16"><circle cx="8" cy="7" r="6" fill="none" stroke="var(--green-light)" stroke-width="1.4"/><path d="M2 7h12M8 1c-3 3-3 9 0 12M8 1c3 3 3 9 0 12" fill="none" stroke="var(--green-light)" stroke-width="1"/><path d="M12 11l5 4" stroke="var(--green-light)" stroke-width="2"/></svg>www.companywebsite.com</li>
      </ul>
    </div>
  </div>
</div>
</body>
</html>
```